Urgent - brand new business card for a startup technical advisory and incubation business in Sydney

We need a brand new business card design for BrightForge. We are a startup technical advisory and incubation business based in Sydney Australia. We work with entrepreneurs and innovators to help rapidly and efficiently turn their ideas into reality and to ensure they have the technical platform required for growth.

Our name is partly inspired by our love of lean product development methods and the lean startup movement.

We would like clean, uncluttered designs that feature our two logo colours and communicate a professional but creative, in-touch and entrepreneurial business.

PLEASE SEE MUST HAVE PRIORITIES FOR DRAFT CONTACT INFORMATION AND OTHER DESIRED TEXT ON CARD.
Updates

We have now updated the brief to include draft business card contact information and also some additional desired text to feature on the card design.    Please review the Must Have priorities.

Also final updated source files for the horizontal and vertical versions have now been uploaded and should be used for any designs.

Thanks!

Target Market(s)

Entrepeneurs, innovators, startup investors looking for a strong product development partner

Industry/Entity Type

Business

Requirements
Must have
• Feature our two logo colours
Be a relatively clean, pared back overall design - quite minimalist

Updated source files (AI) for vertical and horizontal layouts attached.

Draft contact information for business card:
Tom Harcourt
Founder & CTO
Phone: +61 427 555123
Email: xxxx@brightforge.example
Skype: xxxxxharcourt
Twitter: tharcourt

www.brightforge.example

We would also like the overall design to include the phrase "You have great ideas. Let us make them happen." (probably in a reasonably subtle way)

Nice to have
• Inspire me! Double-sided designs are fine with logo, phrase, (URL?) on one side and contact details on other (+ any other design elements)

Logo on business card can be either with lightbulb above the wording as per example here or to the left of the BrightForge wording - both layouts in files provided.
Should not have
• Shouldn't look like a Pendrel Suite business card template :-)

```html
<!DOCTYPE html>
<html lang="en">
<head>
<meta charset="utf-8">
<title>BrightForge business card</title>
<link rel="stylesheet" href="https://fonts.googleapis.com/css2?family=Open+Sans:wght@400;600&display=swap">
<style>
  :root {
    --page: #e9edf0;
    --card: #ffffff;
    --brand-blue: #3a8fd6;
    --ink: #3a3d40;
    --ink-soft: #5b5f63;
    --ink-faint: #8a8f94;
  }
  * { box-sizing: border-box; margin: 0; padding: 0; }
  html, body { width: 1200px; height: 797px; overflow: hidden; }
  body {
    background: var(--page);
    font-family: "Open Sans", Arial, sans-serif;
    color: var(--ink);
    display: flex;
    align-items: center;
    justify-content: center;
    gap: 40px;
  }
  .card {
    position: relative;
    width: 520px;
    height: 297px;
    background: var(--card);
    box-shadow: 0 2px 10px rgba(0,0,0,0.08);
  }
  /* Contact side */
  .contact-side .splash {
    position: absolute;
    left: 18px;
    bottom: 22px;
    width: 120px;
    height: 120px;
    border-radius: 50%;
    background: radial-gradient(circle, rgba(58,143,214,0.85) 0%, rgba(58,143,214,0.35) 60%, rgba(58,143,214,0) 72%);
  }
  .contact-block {
    position: absolute;
    left: 232px;
    top: 52px;
  }
  .person-name {
    font-size: 19px;
    font-weight: 400;
    letter-spacing: 0.5px;
    text-transform: uppercase;
    color: var(--ink);
  }
  .person-role {
    font-size: 11px;
    color: var(--ink-soft);
    margin-top: 2px;
  }
  .contact-lines {
    list-style: none;
    margin-top: 20px;
    font-size: 10.5px;
    line-height: 1.5;
    color: var(--ink-soft);
  }
  .contact-lines .label {
    display: inline-block;
    width: 16px;
    color: var(--brand-blue);
    font-weight: 600;
  }
  .address {
    margin-top: 14px;
    margin-left: 16px;
    font-size: 10.5px;
    line-height: 1.45;
    color: var(--ink-soft);
  }
  /* Logo side */
  .logo-side {
    display: flex;
    flex-direction: column;
    align-items: center;
    justify-content: center;
  }
  .brand-name {
    font-size: 38px;
    font-weight: 600;
    color: var(--brand-blue);
    letter-spacing: 0.5px;
    margin-top: 30px;
  }
  .brand-url {
    margin-top: 12px;
    font-size: 11.5px;
    letter-spacing: 2.5px;
    color: var(--brand-blue);
  }
  .tagline {
    margin-top: 26px;
    font-size: 10.5px;
    letter-spacing: 0.4px;
    color: var(--ink-faint);
  }
</style>
</head>
<body>
  <section class="card contact-side">
    <div class="splash" role="img" aria-label="Soft blue splash decoration in the brand colour"></div>
    <div class="contact-block">
      <h1 class="person-name">Tom Harcourt</h1>
      <p class="person-role">Founder &amp; CTO</p>
      <ul class="contact-lines">
        <li><span class="label">T</span>+61 427 555123</li>
        <li><span class="label">E</span>xxxx@brightforge.example</li>
        <li><span class="label">S</span>xxxxxharcourt</li>
        <li><span class="label">@</span>tharcourt</li>
      </ul>
      <p class="address">Sydney NSW,<br>Australia</p>
    </div>
  </section>

  <section class="card logo-side">
    <p class="brand-name">BrightForge</p>
    <p class="brand-url">www.brightforge.example</p>
    <p class="tagline">You have great ideas. Let us make them happen.</p>
  </section>
</body>
</html>
```